Dentistry

Dentist's personal business card. No logo needed. The card shoul deliver the massage of reliability, professionalism, experience.
Please ad the full brief of the project: down the line it says: the winning look should be precise and pristine NO pictures of Teeth, smiles, instruments etc.

The details to be desplaid are:
Dr. Rob Valdoni
Doctor of Dental Surgery
PHD
Web. Www.drvaldoni.com
Email. Rob@drvaldoni.com
Tel 07731482590
Surgery address. 27Bharwick road London SW4 7QN UK
82 Fenwyn Row London SW3 2HT. Uk

Reason: Decided to make the payment unrefundable in order to get more designers involved.

Requirements
Should not have
• Logo, teeth, smile any sort of instruments.

```html
<!DOCTYPE html>
<html lang="en">
<head>
<meta charset="utf-8">
<title>Rob Valdoni D.M.D – Business Card</title>
<link href="https://fonts.googleapis.com/css2?family=Play:wght@400;700&family=Questrial&display=swap" rel="stylesheet">
<style>
  :root {
    --backdrop: #2e2620;
    --card-paper: #f3f3f1;
    --card-paper-shade: #e6e6e3;
    --ink-dark: #1f2126;
    --ink-grey: #7a7a7a;
    --ink-contact: #55585c;
    --rule: #2a2c30;
  }
  html, body {
    margin: 0;
    padding: 0;
    width: 1200px;
    height: 900px;
    overflow: hidden;
    background: var(--backdrop);
  }
  .canvas {
    position: relative;
    width: 1200px;
    height: 900px;
  }
  .business-card {
    position: absolute;
    left: 180px;
    top: 210px;
    width: 840px;
    height: 480px;
    border-radius: 30px;
    background: linear-gradient(160deg, var(--card-paper) 0%, var(--card-paper) 55%, var(--card-paper-shade) 100%);
    box-shadow: 0 18px 40px rgba(0,0,0,0.45);
  }
  .practice-name {
    position: absolute;
    right: 64px;
    top: 180px;
    margin: 0;
    font-family: "Play", sans-serif;
    font-weight: 700;
    font-size: 21px;
    color: var(--ink-grey);
    letter-spacing: 0.3px;
  }
  .dentist-name {
    position: absolute;
    left: 84px;
    top: 168px;
    margin: 0;
    font-family: "Play", sans-serif;
    font-weight: 700;
    font-size: 31px;
    line-height: 38px;
    color: var(--ink-dark);
    letter-spacing: 0.5px;
  }
  .dentist-degree {
    position: absolute;
    left: 86px;
    top: 208px;
    margin: 0;
    font-family: "Play", sans-serif;
    font-weight: 700;
    font-size: 13px;
    color: var(--ink-dark);
    letter-spacing: 1px;
  }
  .divider-rule {
    position: absolute;
    left: 84px;
    right: 64px;
    top: 236px;
    height: 1.5px;
    background: var(--rule);
  }
  .contact-list {
    position: absolute;
    right: 80px;
    top: 262px;
    margin: 0;
    padding: 0;
    list-style: none;
    font-family: "Questrial", sans-serif;
    font-size: 21px;
    color: var(--ink-contact);
    line-height: 30px;
    white-space: nowrap;
  }
  .contact-item {
    display: flex;
    align-items: flex-start;
  }
  .contact-icon {
    flex: 0 0 30px;
    display: flex;
    justify-content: center;
    padding-top: 8px;
  }
  .contact-at {
    font-weight: 700;
    font-size: 18px;
    padding-top: 0;
    color: var(--ink-dark);
  }
  .address-lines {
    display: flex;
    flex-direction: column;
    align-items: flex-end;
  }
</style>
</head>
<body>
<main class="canvas">
  <article class="business-card">
    <p class="practice-name">Dental care</p>
    <h1 class="dentist-name">Rob Valdoni</h1>
    <p class="dentist-degree">D.M.D</p>
    <div class="divider-rule"></div>
    <ul class="contact-list">
      <li class="contact-item">
        <span class="contact-icon">
          <svg width="14" height="14" viewBox="0 0 14 14" aria-hidden="true">
            <circle cx="7" cy="7" r="6.2" fill="none" stroke="#1f2126" stroke-width="1.4"/>
            <path d="M5 3.8 L6.3 5.4 L5.6 6.3 Q6.4 7.9 7.8 8.6 L8.7 7.8 L10.2 9.1 L9.3 10.2 Q6.2 10 3.9 5 Z" fill="#1f2126"/>
          </svg>
        </span>
        <span>07731482590</span>
      </li>
      <li class="contact-item">
        <span class="contact-icon contact-at">@</span>
        <span>Rob@drvaldoni.com</span>
      </li>
      <li class="contact-item">
        <span class="contact-icon">
          <svg width="12" height="16" viewBox="0 0 12 16" aria-hidden="true">
            <path d="M6 15.5 C3 11 1 8.5 1 5.8 A5 5 0 0 1 11 5.8 C11 8.5 9 11 6 15.5 Z" fill="#1f2126"/>
            <circle cx="6" cy="5.8" r="1.8" fill="#f3f3f1"/>
          </svg>
        </span>
        <span class="address-lines">
          <span>27Bharwick road London</span>
          <span>SW4 7QN UK</span>
        </span>
      </li>
    </ul>
  </article>
</main>
</body>
</html>
```